Thank you for shopping with us business card

We would like a thank you card for our rebranded business. We used to be "Brindle Goods" but are now "Marlow Finds. Old thank you card and new logo will be attached for reference. New thank you card does not have to be same design as old thank you card, but please use new logo.
Shopmart URL is now marlowfinds.shopmart.example
Instagram is @Marlow_Finds
Email is marlowfinds@mailbox.example
Thank you!

Contact Information for Business Card

Shopmart site, email, Instagram

```html
<!DOCTYPE html>
<html lang="en">
<head>
<meta charset="utf-8">
<title>Marlow Finds – Thank You Card</title>
<link rel="stylesheet" href="https://fonts.googleapis.com/css2?family=Montserrat:wght@400;500;600;700;800&display=swap">
<style>
  :root {
    --page: #efe7dd;
    --mustard: #dcaa4b;
    --rose: #b84858;
    --mist: #c6dfe6;
    --navy: #14344f;
    --teal: #457889;
    --slate-blue: #44618a;
    --white: #ffffff;
  }
  * { box-sizing: border-box; margin: 0; padding: 0; }
  html, body {
    width: 1200px; height: 1200px; overflow: hidden;
    background: var(--page);
    font-family: "Montserrat", Arial, sans-serif;
  }
  .canvas {
    width: 1200px; height: 1200px;
    display: flex; flex-direction: column; align-items: center; justify-content: center;
    gap: 60px;
  }
  .card {
    width: 900px; height: 514px;
    position: relative; overflow: hidden;
    box-shadow: 0 6px 18px rgba(20, 52, 79, 0.18);
  }

  /* Thank-you side */
  .thanks-band {
    height: 110px; background: var(--mustard);
    display: flex; align-items: center; justify-content: center;
    padding: 0 36px;
    color: var(--white); font-weight: 800; font-size: 36px; letter-spacing: 2px;
    text-transform: uppercase; white-space: nowrap;
  }
  .message-band {
    height: 110px; background: var(--rose);
    display: flex; align-items: center; padding: 0 36px;
    color: var(--white); font-weight: 500; font-size: 20px; line-height: 1.35;
    letter-spacing: 0.5px; text-transform: uppercase;
  }
  .lower { display: flex; height: 294px; }
  .brand-panel {
    width: 420px; background: var(--mist);
    display: flex; flex-direction: column; align-items: center; justify-content: center; gap: 26px;
    color: var(--navy);
  }
  .brand-mark { width: 110px; height: 110px; background: var(--navy); }
  .brand-name { font-weight: 700; font-size: 30px; letter-spacing: 0.5px; text-transform: uppercase; }
  .contact-list { flex: 1; display: flex; flex-direction: column; }
  .contact-row {
    flex: 1; display: flex; align-items: center; gap: 22px; padding: 0 28px 0 40px;
    color: var(--white); font-size: 19px; font-weight: 500; white-space: nowrap;
  }
  .contact-row--email { background: var(--teal); }
  .contact-row--shop { background: var(--slate-blue); }
  .contact-row--social { background: var(--navy); }
  .contact-icon { width: 40px; height: 40px; flex: none; display: block; }
  .contact-icon--square { background: var(--white); }
  .contact-icon--circle { background: var(--white); border-radius: 50%; }

  /* Brand side */
  .card--brand {
    background: repeating-linear-gradient(135deg,
      var(--navy) 0 190px, var(--teal) 190px 380px);
    display: flex; align-items: center; padding-left: 110px; gap: 50px;
  }
  .cover-mark { width: 150px; height: 150px; background: var(--white); }
  .cover-divider { width: 3px; height: 230px; background: var(--white); }
  .cover-name {
    color: var(--white); font-weight: 600; font-size: 80px; line-height: 1.05;
    text-transform: uppercase; letter-spacing: 1px;
  }
</style>
</head>
<body>
<main class="canvas">
  <section class="card card--thanks">
    <div class="thanks-band">Thank you for your purchase</div>
    <div class="message-band">Your purchase made my day and I hope this package brightens yours. Please come back and leave a review.</div>
    <div class="lower">
      <div class="brand-panel">
        <div class="brand-mark"></div>
        <div class="brand-name">Marlow Finds</div>
      </div>
      <div class="contact-list">
        <div class="contact-row contact-row--email">
          <svg class="contact-icon" viewBox="0 0 44 44" aria-hidden="true">
            <rect x="4" y="10" width="36" height="24" fill="none" stroke="#fff" stroke-width="2.5"/>
            <polyline points="4,10 22,24 40,10" fill="none" stroke="#fff" stroke-width="2.5"/>
            <line x1="4" y1="34" x2="17" y2="20" stroke="#fff" stroke-width="2"/>
            <line x1="40" y1="34" x2="27" y2="20" stroke="#fff" stroke-width="2"/>
          </svg>
          <span>marlowfinds@mailbox.example</span>
        </div>
        <div class="contact-row contact-row--shop">
          <span class="contact-icon contact-icon--square"></span>
          <span>marlowfinds.shopmart.example</span>
        </div>
        <div class="contact-row contact-row--social">
          <span class="contact-icon contact-icon--circle"></span>
          <span>@Marlow_Finds</span>
        </div>
      </div>
    </div>
  </section>

  <section class="card card--brand">
    <div class="cover-mark"></div>
    <div class="cover-divider"></div>
    <div class="cover-name">Marlow<br>Finds</div>
  </section>
</main>
</body>
</html>
```